WHAT COMES NEXT? Discovering the reason for being beside the Inner Lamp

Creating a book that is about living a spiritual life. The book is about letting go of the materialistic world and finding happiness through self realisation and enlightenment. The contents page is below that gives an idea of what is contained in the book.

The book is based on the writings of the Sikhs - from India. But it is written in a universal way that is understandable to all.

CONTENTS
Living for a purpose
- Born to be original! Dying as a copy!
- My relationship with everything but me!
- What is my purpose?

Life as a human being!
- Stages of Life
- Five Weaknesses

What is driving our lives?
- Information overload?
- What are your drivers?
- Giving life meaning

You reap what you sow
- Is my destiny written?
- Good and bad actions
- Maya – the illusion and it’s three modes

Slow down and let go
- The mind in overdrive
- Being aware of our mental health
- Why Slow Down?

The Guidance of the Guru
- Why do I need a Guru?
- What the Guru gives you
- Gurbani – the Guru’s Words

Staying connected
- Repeating the Mantra
- Doing two things at once
- Remembering in times of difficulty

Cultivating virtues
- Theory vs Practice
- Virtues and true religion
- Some key virtues

The Mystical Creation
- Experiencing ecstasy
- Enlightenment and intuition
- Spiritual Transformation

Good Company
- How do my companions affect me?
- The company of Saintly people
- Obtaining the fruits that the Guru describes

Serving selflessly
- Serving is our purpose
- Being grateful
- Being generous

Ten things to change your life today

Target Market(s)

All those who want to learn about spirituality. We are targeting young and middle aged but not necessarily ruling out older demographic.

Requirements
Must have
• The book cover:

- exciting and intriguing
- theme is "why am I here" in this world
- some kind of lean towards enlightenment
Nice to have
• It is not essential but the cover could subtly show something about the Sikh faith. Can discuss this further if necessary.
Should not have
• Should not:

- look dull and boring
- don't want it to look like a Buddhism book

```html
<!DOCTYPE html>
<html lang="en">
<head>
<meta charset="utf-8">
<title>What Comes Next? — Book Cover</title>
<link href="https://fonts.googleapis.com/css2?family=Alex+Brush&family=Libre+Baskerville:wght@400;700&display=swap" rel="stylesheet">
<style>
  :root {
    --backdrop: #dcdcd8;
    --ink: #1e2b2c;
    --ink-warm: #4a2a22;
    --teal: #2f7f86;
    --accent-red: #c0262a;
    --sun: #f4d21c;
    --amber: #e88a1e;
    --cream: #fbf2d6;
    --deep-blue: #1f3d6b;
    --serif: "Libre Baskerville", Georgia, serif;
    --script: "Alex Brush", cursive;
  }
  * { box-sizing: border-box; margin: 0; padding: 0; }
  html, body { width: 1200px; height: 853px; overflow: hidden; }
  body { background: var(--backdrop); position: relative; }

  .cover {
    position: absolute; left: 315px; top: 20px;
    width: 569px; height: 813px; overflow: hidden;
    background: var(--cream);
  }
  .cover-artwork {
    position: absolute; inset: 0;
    background:
      radial-gradient(ellipse 22% 30% at 14% 72%, rgba(31,61,107,.85), transparent 70%),
      radial-gradient(ellipse 18% 40% at 24% 80%, rgba(224,96,30,.8), transparent 70%),
      radial-gradient(ellipse 14% 35% at 5% 80%, rgba(30,120,110,.85), transparent 70%),
      radial-gradient(ellipse 12% 22% at 20% 15%, rgba(200,60,30,.7), transparent 70%),
      linear-gradient(90deg, rgba(242,200,20,1) 0%, rgba(244,214,40,.95) 30%, rgba(248,228,140,.8) 55%, rgba(251,242,214,.4) 80%, transparent 100%),
      linear-gradient(180deg, #f8d93a 0%, #f7e48a 35%, var(--cream) 75%, #fdf6ea 100%);
  }

  .tagline {
    position: absolute; right: 22px; top: 45px;
    font: 700 11px/1 var(--serif); letter-spacing: .02em;
    color: var(--ink-warm);
  }
  .title { position: absolute; right: 22px; top: 60px; text-align: right; }
  .title-script {
    display: block;
    font: 400 190px/1 var(--script);
    color: var(--ink);
    background: linear-gradient(100deg, var(--ink) 20%, var(--ink-warm) 50%, var(--ink) 80%);
    -webkit-background-clip: text; background-clip: text;
    -webkit-text-fill-color: transparent;
  }
  .title-serif {
    display: block; margin-top: -30px;
    font: 400 44px/1 var(--serif);
    color: var(--ink);
  }

  .subtitle {
    position: absolute; left: 357px; top: 665px; width: 200px;
    font: 400 15px/1.35 var(--serif);
    color: var(--ink-warm);
  }
  .subtitle .teal { color: var(--teal); }
  .subtitle .highlight { color: var(--accent-red); }

  .author {
    position: absolute; left: 357px; top: 756px;
    font: 400 11px/1 var(--serif);
    color: var(--ink);
  }
</style>
</head>
<body>
  <div class="cover">
    <div class="cover-artwork" role="img" aria-label="Expressive painted artwork in yellow, orange, teal and blue showing a standing figure in profile, fading to cream on the right"></div>

    <p class="tagline">EXCITING AND INTRIGUING</p>

    <h1 class="title">
      <span class="title-script">What</span>
      <span class="title-serif">comes next?</span>
    </h1>

    <p class="subtitle">
      <span class="teal">Discovering the</span> reason for being beside the <span class="highlight">Inner Lamp</span>
    </p>

    <p class="author">By: Navdeep Arora</p>
  </div>
</body>
</html>
```